Hi,

I would like to have a invitation made for a party. exactly like the picture in the link below.

http://pinboardia.example/pin/730215948361027459/

However, Please change the colors into fun/ girly feeling. font can be different and size of the card should be the same

Name of the girl: RINA
What: Bachelorette Party
Where:TOLO Boat
Dubai Coral Quay Sailing Club
When:7th of February 2013

No RSVP required. (so no need to put it)

```html
<!DOCTYPE html>
<html lang="en">
<head>
<meta charset="utf-8">
<title>Rina's Bachelorette Party Invitation</title>
<link rel="stylesheet" href="https://fonts.googleapis.com/css2?family=Fredoka+One&family=Sniglet:wght@800&family=Oswald:wght@500;600&family=Stint+Ultra+Condensed&display=swap">
<style>
  :root {
    --violet: #6a00ff;
    --magenta: #ff00ff;
    --paper: #fff2fc;
    --paper-blush: #ffe4f8;
    --frame-lilac: #b77cff;
    --corner-lilac: #a35cff;
    --white: #ffffff;
  }
  * { box-sizing: border-box; margin: 0; padding: 0; }
  html, body {
    width: 1200px;
    height: 960px;
    overflow: hidden;
    background: var(--violet);
  }
  .invitation {
    position: absolute;
    left: 40px;
    top: 120px;
    width: 1120px;
    height: 720px;
    display: flex;
    box-shadow: 0 6px 0 rgba(0,0,0,0.35);
  }
  .panel { position: relative; height: 100%; }
  .panel--cover {
    width: 560px;
    background: linear-gradient(90deg, var(--paper) 0%, #fff8fd 100%);
  }
  .panel--inside-left {
    width: 280px;
    background: linear-gradient(90deg, var(--paper-blush) 0%, var(--paper) 60%);
    border-left: 1px solid #f3d2ee;
  }
  .panel--details {
    width: 280px;
    background: linear-gradient(90deg, var(--paper-blush) 0%, var(--paper) 40%);
    border-left: 1px solid #f3d2ee;
  }
  .corner-ornament {
    position: absolute;
    width: 70px;
    height: 70px;
    background: var(--corner-lilac);
    opacity: 0.55;
  }
  .corner-ornament--top-right {
    top: 28px; right: 30px;
    clip-path: polygon(0 0, 100% 0, 100% 100%, 82% 100%, 82% 18%, 0 18%);
  }
  .corner-ornament--bottom-left {
    bottom: 30px; left: 30px;
    clip-path: polygon(0 0, 18% 0, 18% 82%, 100% 82%, 100% 100%, 0 100%);
  }
  .divider-ornament {
    position: absolute;
    left: 30px;
    top: 255px;
    width: 220px;
    height: 26px;
    background: linear-gradient(90deg, transparent 0%, var(--magenta) 20%, var(--corner-lilac) 50%, var(--magenta) 80%, transparent 100%);
    clip-path: polygon(0 50%, 40% 40%, 50% 0, 60% 40%, 100% 50%, 60% 60%, 50% 100%, 40% 60%);
  }
  .headline {
    position: absolute;
    left: 40px;
    top: 0;
    width: 840px;
    height: 720px;
    pointer-events: none;
  }
  .headline__name {
    font-family: "Sniglet", "Fredoka One", cursive;
    font-weight: 800;
    font-size: 150px;
    fill: var(--magenta);
  }
  .headline__tagline {
    font-family: "Stint Ultra Condensed", "Oswald", serif;
    font-size: 118px;
    fill: var(--violet);
  }
  .headline__single {
    font-family: "Fredoka One", "Sniglet", sans-serif;
    font-size: 250px;
  }
  .details-frame {
    position: absolute;
    left: 22px;
    top: 80px;
    width: 236px;
    height: 560px;
    background: var(--frame-lilac);
  }
  .details-card {
    position: absolute;
    left: 38px;
    top: 96px;
    width: 204px;
    height: 528px;
    background: var(--white);
    display: flex;
    flex-direction: column;
    justify-content: space-around;
    align-items: center;
    padding: 40px 6px;
    text-align: center;
    font-family: "Oswald", sans-serif;
  }
  .detail__label {
    color: var(--violet);
    font-weight: 500;
    font-size: 17px;
    line-height: 1.4;
  }
  .detail__value {
    color: var(--magenta);
    font-weight: 600;
    font-size: 17px;
    line-height: 1.5;
  }
</style>
</head>
<body>
  <main class="invitation">
    <section class="panel panel--cover">
      <div class="corner-ornament corner-ornament--top-right" role="img" aria-label="Lilac floral corner flourish"></div>
      <div class="corner-ornament corner-ornament--bottom-left" role="img" aria-label="Lilac floral corner flourish"></div>
    </section>
    <section class="panel panel--inside-left">
      <div class="divider-ornament" role="img" aria-label="Magenta decorative divider with central flourish"></div>
    </section>
    <section class="panel panel--details">
      <div class="details-frame" role="img" aria-label="Ornate lilac scrollwork frame"></div>
      <div class="details-card">
        <p class="detail"><span class="detail__label">Name of the girl:</span><br><span class="detail__value">RINA</span></p>
        <p class="detail"><span class="detail__label">What:</span><br><span class="detail__value">Bachelorette Party</span></p>
        <p class="detail"><span class="detail__label">Where:</span><br><span class="detail__value">TOLO Boat<br>Dubai Coral Quay Sailing Club</span></p>
        <p class="detail"><span class="detail__label">When:</span><br><span class="detail__value">7th of February 2013</span></p>
      </div>
    </section>

    <svg class="headline" viewBox="0 0 840 720" xmlns="http://www.w3.org/2000/svg">
      <defs>
        <linearGradient id="single-gradient" x1="0" y1="0" x2="0" y2="1">
          <stop offset="0" stop-color="#6a00ff"/>
          <stop offset="1" stop-color="#ff00ff"/>
        </linearGradient>
        <text id="single-word" class="headline__single" x="390" y="640" text-anchor="middle" textLength="740" lengthAdjust="spacingAndGlyphs">SinGLE</text>
      </defs>

      <text class="headline__name" x="70" y="250" textLength="430" lengthAdjust="spacingAndGlyphs">rina</text>
      <path class="headline__heart" fill="#ff00ff" d="M528 150 c-10 -16 -32 -8 -26 10 c4 10 16 18 26 26 c10 -8 22 -16 26 -26 c6 -18 -16 -26 -26 -10z"/>
      <text class="headline__name" x="560" y="250" textLength="70" lengthAdjust="spacingAndGlyphs">s</text>

      <text class="headline__tagline" x="30" y="395" textLength="800" lengthAdjust="spacingAndGlyphs">LAST CHANCE TO CELEBRATE BEING</text>

      <use href="#single-word" fill="none" stroke="url(#single-gradient)" stroke-width="28" stroke-linejoin="round"/>
      <use href="#single-word" fill="none" stroke="#ffffff" stroke-width="14" stroke-linejoin="round"/>
      <use href="#single-word" fill="url(#single-gradient)"/>
    </svg>
  </main>
</body>
</html>
```